Clear Strand Record Format Sticker

We need a set of stickers (~5-7cm) to promote the Clear Strand Record Format. Most of the people we will be handing these out to are technically minded (network operators, open-source coders, Internet standards folk, Internet measurement researchers). The design should include the CSRF icon and colour scheme (see here https://strandrecord.example/en/resources/).

Target Market(s)

network operators, open-source coders, Internet standards folk, Internet measurement researchers

• Hind

```html
<!DOCTYPE html>
<html lang="en">
<head>
<meta charset="utf-8">
<title>Clear Strand Record Format Sticker</title>
<link rel="stylesheet" href="https://fonts.googleapis.com/css2?family=Roboto+Condensed:wght@400;500&family=Montserrat:wght@600&display=swap">
<style>
  :root {
    --backdrop: #e9e6e1;
    --sticker-navy: #11132b;
    --map-tone: #2a2e4a;
    --accent-lime: #b5cc2e;
    --mark-white: #ffffff;
  }
  html, body {
    margin: 0;
    padding: 0;
    width: 1200px;
    height: 1002px;
    overflow: hidden;
    background: var(--backdrop);
  }
  .canvas {
    position: relative;
    width: 1200px;
    height: 1002px;
  }
  .sticker {
    position: absolute;
    left: 94px;
    top: 140px;
    width: 1012px;
    height: 722px;
    border-radius: 22px;
    background: var(--sticker-navy);
    overflow: hidden;
  }
  .world-network-map {
    position: absolute;
    left: 0;
    top: 280px;
    width: 1012px;
    height: 442px;
    background: radial-gradient(ellipse 70% 80% at 50% 75%, var(--map-tone) 0%, rgba(42,46,74,0.45) 55%, rgba(17,19,43,0) 100%);
  }
  .wordmark {
    position: absolute;
    left: 0;
    right: 0;
    top: 20px;
    margin: 0;
    text-align: center;
    font-family: "Roboto Condensed", sans-serif;
    font-weight: 500;
    font-size: 250px;
    line-height: 1;
    letter-spacing: 2px;
    color: var(--mark-white);
  }
  .tagline {
    position: absolute;
    margin: 0;
    font-family: "Roboto Condensed", sans-serif;
    font-weight: 400;
    font-size: 57px;
    line-height: 1;
    color: var(--accent-lime);
    white-space: nowrap;
  }
  .tagline--first { left: 49px; top: 338px; }
  .tagline--second { left: 104px; top: 427px; }
  .web-address {
    position: absolute;
    left: 311px;
    top: 635px;
    margin: 0;
    font-family: "Montserrat", sans-serif;
    font-weight: 600;
    font-size: 29px;
    color: var(--accent-lime);
  }
</style>
</head>
<body>
  <main class="canvas">
    <section class="sticker">
      <div class="world-network-map" role="img" aria-label="Faint world map overlaid with a web of connected network nodes"></div>
      <h1 class="wordmark">csrf</h1>
      <p class="tagline tagline--first">Mapping The World,s Internet Backdone</p>
      <p class="tagline tagline--second">Stronger Networks for Everyone.</p>
      <p class="web-address">www.strandrecord.example</p>
    </section>
  </main>
</body>
</html>
```